Design logo and business card.

Design and construct logo and card for my business which is an over seeing company of other smaller businesses. The companies name is quarry5 business collective. Im open to any ideas but i am looking for a very cool contemporary design with a very prestige feel. The card can be either single or double sided, Thank you and i will look forward to your submissions.

Industry/Entity Type

Business

Requirements
Must have
• Company name, email, website, telephone, my name. Cool modern look with a prestige feel.

```html
<!DOCTYPE html>
<html lang="en">
<head>
<meta charset="utf-8">
<title>Quarry5 Business Collective — Business Card</title>
<link rel="stylesheet" href="https://fonts.googleapis.com/css2?family=Bebas+Neue&display=swap">
<style>
  :root {
    --stone-light: #d2d2d2;
    --stone-mid: #bdbdbd;
    --charcoal: #222222;
    --ink: #262626;
    --paper-text: #ececec;
  }
  html, body {
    margin: 0;
    padding: 0;
    width: 1200px;
    height: 686px;
    overflow: hidden;
    background: var(--charcoal);
  }
  .card {
    position: relative;
    width: 1200px;
    height: 686px;
    overflow: hidden;
    font-family: "Bebas Neue", "Arial Narrow", sans-serif;
  }
  .card__brand-band {
    position: absolute;
    left: 0;
    top: 0;
    width: 1200px;
    height: 342px;
    display: flex;
    align-items: center;
    justify-content: center;
    background:
      radial-gradient(ellipse at 30% 40%, var(--stone-light) 0%, transparent 60%),
      radial-gradient(ellipse at 75% 70%, var(--stone-light) 0%, transparent 55%),
      var(--stone-mid);
  }
  .brand-name {
    margin: 0;
    color: var(--ink);
    font-size: 64px;
    font-weight: 400;
    letter-spacing: 8px;
    line-height: 1;
    white-space: nowrap;
  }
  .card__contact-band {
    position: absolute;
    left: 0;
    top: 342px;
    width: 1200px;
    height: 344px;
    background: var(--charcoal);
  }
  .contact {
    position: absolute;
    top: 438px;
    width: 600px;
    text-align: center;
    color: var(--paper-text);
    font-size: 40px;
    letter-spacing: 5px;
    line-height: 76px;
  }
  .contact--person { left: 0; }
  .contact--company { left: 600px; }
  .contact p { margin: 0; }
</style>
</head>
<body>
  <main class="card">
    <section class="card__brand-band">
      <h1 class="brand-name">QUARRY5 BUSINESS COLLECTIVE</h1>
    </section>
    <section class="card__contact-band"></section>
    <div class="contact contact--person">
      <p class="contact__name">JOHN S. DOE</p>
      <p class="contact__email">NAME@EMAIL.COM</p>
    </div>
    <div class="contact contact--company">
      <p class="contact__web">QUARRY5.COM</p>
      <p class="contact__phone">XXX.XXX.XXXX</p>
    </div>
  </main>
</body>
</html>
```